Health Care Company with Logo Needs Business Cards designed

We are a luxury behavioral health company looking for business cards design we already have a logo and are looking for someone to design a sophisticated luxurious looking business card. Please note that Card design should be captivating just like the logo and also encompass the logo color

Industry/Entity Type

Healthcare

Contact Information for Business Card

Logo,company name, tagline, my name and title, contact details, and physical address

```html
<!DOCTYPE html>
<html lang="en">
<head>
<meta charset="utf-8">
<title>Orrin Wellness Group – Business Card</title>
<link href="https://fonts.googleapis.com/css2?family=Roboto:wght@400;500;700&family=Roboto+Condensed:wght@700&display=swap" rel="stylesheet">
<style>
  :root {
    --bg: #1e1e1e;
    --purple: #7f3f98;
    --purple-deep: #4b1f60;
    --white: #ffffff;
  }
  * { box-sizing: border-box; margin: 0; padding: 0; }
  html, body { width: 1200px; height: 1015px; overflow: hidden; }
  body {
    background: var(--bg);
    font-family: "Roboto", Arial, sans-serif;
    position: relative;
  }
  .card {
    position: absolute;
    left: 320px;
    width: 560px;
    height: 320px;
    box-shadow: 0 14px 30px rgba(0,0,0,.55);
    overflow: hidden;
  }
  .card--front { top: 150px; background: var(--purple); }
  .card--back { top: 545px; background: var(--white); }

  .brand {
    position: absolute;
    display: flex;
    align-items: center;
    gap: 12px;
  }
  .brand__mark {
    width: 40px; height: 40px;
    flex: none;
  }
  .brand__name {
    font-weight: 500;
    font-size: 30px;
    line-height: 1;
    white-space: nowrap;
  }
  .brand__tagline {
    margin-top: 6px;
    font-size: 11px;
    font-weight: 400;
    letter-spacing: 1px;
    white-space: nowrap;
  }

  .card--front .brand { left: 110px; top: 134px; }
  .card--front .brand__mark { background: var(--purple-deep); }
  .card--front .brand__name,
  .card--front .brand__tagline { color: var(--purple-deep); }

  .back__logo-area {
    position: absolute; left: 0; top: 0; width: 272px; height: 100%;
  }
  .card--back .brand { left: 34px; top: 142px; gap: 9px; }
  .card--back .brand__mark { width: 26px; height: 26px; background: var(--purple); }
  .card--back .brand__name { color: var(--purple); font-size: 20px; }
  .card--back .brand__tagline { color: var(--purple); font-size: 8px; letter-spacing: .6px; margin-top: 4px; }

  .back__panel {
    position: absolute; right: 0; top: 0;
    width: 288px; height: 100%;
    background: var(--purple);
    color: var(--white);
    padding: 62px 20px 0 34px;
  }
  .person__name {
    font-family: "Roboto Condensed", "Arial Narrow", sans-serif;
    font-weight: 700; font-size: 25px; line-height: 1;
  }
  .person__title { font-size: 15px; margin-top: 3px; }
  .contact { list-style: none; margin-top: 18px; }
  .contact__item {
    display: flex; align-items: center; gap: 8px;
    font-size: 14px; line-height: 21px;
  }
  .contact__icon { width: 13px; height: 13px; flex: none; }
  .address { margin-top: 10px; margin-left: 21px; font-size: 14px; line-height: 18px; font-style: normal; }
</style>
</head>
<body>

<section class="card card--front" aria-label="Card front">
  <div class="brand">
    <span class="brand__mark"></span>
    <div>
      <div class="brand__name">Orrin Wellness Group</div>
      <div class="brand__tagline">Calm care for every season</div>
    </div>
  </div>
</section>

<section class="card card--back" aria-label="Card back">
  <div class="back__logo-area">
    <div class="brand">
      <span class="brand__mark"></span>
      <div>
        <div class="brand__name">Orrin Wellness Group</div>
        <div class="brand__tagline">Calm care for every season</div>
      </div>
    </div>
  </div>

  <div class="back__panel">
    <div class="person__name">Daniel Mercer</div>
    <div class="person__title">Managing Director</div>
    <ul class="contact">
      <li class="contact__item">
        <svg class="contact__icon" viewBox="0 0 24 24" fill="var(--white)"><path d="M6.6 10.8a15.1 15.1 0 0 0 6.6 6.6l2.2-2.2c.3-.3.7-.4 1-.2 1.1.4 2.3.6 3.6.6.6 0 1 .4 1 1V20c0 .6-.4 1-1 1A17 17 0 0 1 3 4c0-.6.4-1 1-1h3.5c.6 0 1 .4 1 1 0 1.3.2 2.5.6 3.6.1.3 0 .7-.2 1z"/></svg>
        044-555 010 234
      </li>
      <li class="contact__item">
        <svg class="contact__icon" viewBox="0 0 24 24" fill="none" stroke="var(--white)" stroke-width="2"><rect x="2" y="5" width="20" height="14"/><path d="M2 5l10 8 10-8"/></svg>
        hello@orrinwellness.com
      </li>
      <li class="contact__item">
        <svg class="contact__icon" viewBox="0 0 24 24" fill="none" stroke="var(--white)" stroke-width="2"><circle cx="12" cy="12" r="10"/><path d="M2 12h20M12 2c3 3 3 17 0 20M12 2c-3 3-3 17 0 20"/></svg>
        www.orrinwellness.com
      </li>
    </ul>
    <address class="address">18 Linden Row, Suite 4<br>45001, Riverton</address>
  </div>
</section>

</body>
</html>
```